Website Design for Brewlane Supply Group

BSG is an office refreshments provider. We provide offices with coffee supplies, coffee equipment, water equipment, office products, and breakroom supplies, such as creamers, sugar, stirrers, paper plates, napkins, etc. We also offer green/eco-friendly br

```html
<!DOCTYPE html>
<html lang="en">
<head>
<meta charset="utf-8">
<title>Brewlane Supply Group – Breakroom Supplies</title>
<link href="https://fonts.googleapis.com/css2?family=Bebas+Neue&family=Oswald:wght@500&family=PT+Sans+Narrow:wght@400;700&family=Gelasio:wght@400;500&display=swap" rel="stylesheet">
<style>
:root{
  --espresso:#3a2216;
  --espresso-deep:#2e1a10;
  --gold:#c9a96e;
  --gold-dark:#b08a4e;
  --caramel:#b98a50;
  --cream:#f6f4ef;
  --paper:#faf9f6;
  --ink:#2a1e17;
  --text:#3d352f;
  --tick:#a3231c;
  --button-top:#ffd45a;
  --button-bottom:#f7b51d;
  --footer-text:#8a6a52;
}
*{margin:0;padding:0;box-sizing:border-box}
html,body{width:960px;height:1200px;overflow:hidden}
body{position:relative;background:var(--paper);font-family:"PT Sans Narrow",sans-serif;color:var(--text)}
.top-strip{position:absolute;left:0;top:0;width:960px;height:8px;background:var(--espresso)}
.hero-art{position:absolute;left:0;top:8px}
.nav-bar{position:absolute;left:0;top:8px;width:960px;height:48px;background:rgba(250,247,240,.82)}
.brand{position:absolute;left:77px;top:8px;width:200px;height:91px;background:#fff;box-shadow:0 2px 6px rgba(0,0,0,.25);display:flex;align-items:center;justify-content:center;gap:8px}
.brand-mark{width:14px;height:14px;border-radius:50%;background:var(--espresso)}
.brand-name{font-family:"PT Sans Narrow",sans-serif;font-weight:700;font-size:17px;color:var(--espresso);line-height:1.05;text-align:center}
.main-nav{position:absolute;top:19px;left:318px;display:flex;align-items:center}
.main-nav a{font-family:"Oswald",sans-serif;font-weight:500;font-size:12.5px;color:var(--espresso);text-decoration:none;text-transform:uppercase;height:26px;line-height:26px;margin-right:23px;letter-spacing:-.1px}
.main-nav a.active{background:var(--espresso);color:#fff;padding:0 12px;border-radius:3px;margin-right:21px}
.green-badge{position:absolute;left:828px;top:14px;width:36px;height:36px;border-radius:50%;background:#3f6f8e;border:3px solid #7aa24a}
.hero-title{position:absolute;left:78px;top:136px;font-family:"Bebas Neue",sans-serif;font-size:36px;color:var(--ink);letter-spacing:.3px}
.hero-lead{position:absolute;left:80px;top:175px;width:410px;font-size:12px;line-height:19px;color:var(--ink)}
.hero-points{position:absolute;left:78px;top:248px;list-style:none}
.hero-points li{height:26px;font-size:12px;color:var(--ink);display:flex;align-items:center;gap:9px}
.hero-points svg{flex:none}
.product-ring{position:absolute;left:569px;top:128px;width:228px;height:228px;border-radius:50%;background:rgba(255,255,255,.45);display:flex;align-items:center;justify-content:center}
.product-photo{width:152px;height:190px;border-radius:6px;background:linear-gradient(180deg,#5a5a5c 0%,#9a9a9e 45%,#d8d8da 75%,#3a3a3c 100%)}
.asterisk{position:absolute;left:619px;top:142px;color:#d01c1c;font-size:22px;font-family:Arial,sans-serif}
.slider-dots{position:absolute;left:469px;top:370px;display:flex;gap:4px}
.slider-dots span{width:10px;height:10px;border-radius:50%;background:#fff;border:2px solid #d9cfc0}
.intro{position:absolute;left:85px;top:448px;width:790px;text-align:center;font-family:"Gelasio",serif;font-size:18.5px;line-height:27.5px;color:var(--ink)}
.double-rule{position:absolute;left:102px;width:760px;height:5px;border-top:1.5px solid var(--gold);border-bottom:1.5px solid var(--gold)}
.services{position:absolute;left:0;top:582px;width:960px}
.service{position:absolute;top:0;width:190px}
.service h2{font-family:"Bebas Neue",sans-serif;font-weight:400;font-size:20px;color:var(--caramel);text-align:center;letter-spacing:.2px}
.service-photo{width:100px;height:124px;margin:14px auto 0;border-radius:4px}
.service-photo.brewer{background:linear-gradient(160deg,#4a4c50 0%,#1e1f22 60%,#c8c8c8 100%)}
.service-photo.cup{background:linear-gradient(180deg,#f4f1ea 0%,#dfe8c9 50%,#eec79a 85%,#f4f1ea 100%)}
.service p{font-size:11.5px;line-height:19px;color:var(--ink);margin-top:19px;padding-left:0}
.read-more{display:block;width:90px;height:32px;margin:13px auto 0;background:linear-gradient(180deg,var(--button-top),var(--button-bottom));border:1px solid #e9a618;font-size:11.5px;color:var(--ink);text-align:center;line-height:30px;text-decoration:none}
.partners-title{position:absolute;left:103px;top:952px;font-family:"Gelasio",serif;font-size:17px;color:var(--ink)}
.partners{position:absolute;top:993px;left:0;width:960px}
.partner{position:absolute;width:138px;height:121px;background:var(--gold);border-radius:8px}
.site-footer{position:absolute;left:0;top:1150px;width:960px;height:50px;background:var(--espresso-deep)}
.copyright{position:absolute;left:74px;top:18px;font-size:11px;color:var(--footer-text)}
.footer-links{position:absolute;right:90px;top:18px;font-size:11px;color:var(--footer-text)}
.footer-links a{color:var(--footer-text);text-decoration:none}
</style>
</head>
<body>
<div class="top-strip"></div>

<svg class="hero-art" width="960" height="440" viewBox="0 0 960 440">
  <defs>
    <linearGradient id="roomTone" x1="0" y1="0" x2="0" y2="1">
      <stop offset="0" stop-color="#eeebe4"/>
      <stop offset=".45" stop-color="#e6dfd2"/>
      <stop offset=".7" stop-color="#b88f5a"/>
      <stop offset="1" stop-color="#8a5e32"/>
    </linearGradient>
    <clipPath id="heroClip"><path d="M0 0 H960 V292 Q480 552 0 292 Z"/></clipPath>
  </defs>
  <rect role="img" aria-label="Blurred photo of a bright conference room with a long wooden table" width="960" height="440" fill="url(#roomTone)" clip-path="url(#heroClip)"/>
  <path d="M0 292 Q480 552 960 292" fill="none" stroke="#6b4323" stroke-width="4"/>
  <path d="M0 298 Q480 562 960 298" fill="none" stroke="var(--gold)" stroke-width="8"/>
</svg>

<header>
  <div class="nav-bar"></div>
  <div class="brand"><span class="brand-mark"></span><span class="brand-name">Brewlane Supply Group</span></div>
  <nav class="main-nav">
    <a class="active" href="#">Home</a>
    <a href="#">About Us</a>
    <a href="#">Coffee Service</a>
    <a href="#">Breakroom Supplies</a>
    <a href="#">Go Green</a>
    <a href="#">Contact Us</a>
  </nav>
  <div class="green-badge"></div>
</header>

<section class="hero">
  <h1 class="hero-title">Breakroom Supplies</h1>
  <p class="hero-lead">Lorem ipsum dolor sit amet, consectetur adipiscing elit. Cras dolor orci, eleifend at mattis id, condimentum a metus. In hac habitasse platea dictumst. Maecenas scelerisque quam leo. Nulla iaculis sem ac dolor fringilla eget gravida dui gravida.</p>
  <ul class="hero-points">
    <li><svg width="14" height="12" viewBox="0 0 14 12"><path d="M1 6 L5 10 L13 1" fill="none" stroke="var(--tick)" stroke-width="2.6"/></svg>Lorem ipsum dolor sit amet, consectetur adipiscing elit.</li>
    <li><svg width="14" height="12" viewBox="0 0 14 12"><path d="M1 6 L5 10 L13 1" fill="none" stroke="var(--tick)" stroke-width="2.6"/></svg>Cras dolor orci, eleifend at mattis id, condimentum a metus.</li>
    <li><svg width="14" height="12" viewBox="0 0 14 12"><path d="M1 6 L5 10 L13 1" fill="none" stroke="var(--tick)" stroke-width="2.6"/></svg>In hac habitasse platea dictumst.</li>
    <li><svg width="14" height="12" viewBox="0 0 14 12"><path d="M1 6 L5 10 L13 1" fill="none" stroke="var(--tick)" stroke-width="2.6"/></svg>Maecenas scelerisque quam leo. Nulla iaculis sem</li>
  </ul>
  <div class="product-ring"><div class="product-photo" role="img" aria-label="Photo of an automatic espresso machine with bean hoppers"></div></div>
  <span class="asterisk">*</span>
  <div class="slider-dots"><span></span><span></span><span></span><span></span></div>
</section>

<p class="intro">At Brewlane Supply Group, we help your company eliminate all of the hassles of dealing with bottled water, office coffee and pantry supplies. Breakrooms should be there to help you do your job, not be your job.</p>

<div class="double-rule" style="top:541px"></div>

<section class="services">
  <article class="service" style="left:86px">
    <h2>Office Coffee Service</h2>
    <div class="service-photo brewer" role="img" aria-label="Photo of a single-cup coffee brewer with a mug"></div>
    <p style="margin-left:9px">Whether you choose Traditional Brewers, Single-Cup Coffee or Espresso Machines, our commitment to excellence ensures the same delicious and satisfying cup time and again..</p>
    <a class="read-more" href="#">Read More</a>
  </article>
  <article class="service" style="left:285px">
    <h2>Breakroom Supplies</h2>
    <div class="service-photo cup" role="img" aria-label="Photo of an eco-friendly paper cup with a leaf print"></div>
    <p style="margin-left:10px">Leafline Beverage Systems can fully stock your break room, kitchen, or pantry with all the essentials for a comfortable and inviting retreat from the daily grind. Our extensive selection of breakroom...</p>
    <a class="read-more" href="#">Read More</a>
  </article>
  <article class="service" style="left:496px">
    <h2>Office Coffee Service</h2>
    <div class="service-photo brewer" role="img" aria-label="Photo of a single-cup coffee brewer with a mug"></div>
    <p style="margin-left:9px">Whether you choose Traditional Brewers, Single-Cup Coffee or Espresso Machines, our commitment to excellence ensures the same delicious and satisfying cup time and again..</p>
    <a class="read-more" href="#">Read More</a>
  </article>
  <article class="service" style="left:691px">
    <h2>Breakroom Supplies</h2>
    <div class="service-photo cup" role="img" aria-label="Photo of an eco-friendly paper cup with a leaf print"></div>
    <p style="margin-left:12px">Leafline Beverage Systems can fully stock your break room, kitchen, or pantry with all the essentials for a comfortable and inviting retreat from the daily grind. Our extensive selection of breakroom...</p>
    <a class="read-more" href="#">Read More</a>
  </article>
</section>

<div class="double-rule" style="top:932px"></div>

<h3 class="partners-title">Our Partners</h3>
<section class="partners">
  <div class="partner" style="left:103px"></div>
  <div class="partner" style="left:258px"></div>
  <div class="partner" style="left:415px"></div>
  <div class="partner" style="left:571px"></div>
  <div class="partner" style="left:731px"></div>
</section>

<footer class="site-footer">
  <p class="copyright">Copyright © 2012 Company Naame.  All right reserved.</p>
  <p class="footer-links"><a href="#">Term of Use</a> |&nbsp;&nbsp; <a href="#">Privacy Policy</a> |&nbsp;&nbsp; <a href="#">Contact</a></p>
</footer>
</body>
</html>
```